co working space / serviced office/ business centre

Vandrel - vandrel.in, is a very young brand bieng run by 3 young entrepreneurs. We want to be become out of the league company delivering fabulous and beautiful serviced offices in India and abroad. We hire designers who have made spaces across the world. We want to get visiting card design which gives complete fresh look to the people who carries that card, has to be very impactful and should symbolise happy young and energetic brand. should be completely out of the box thinking of international level, should portray global brand image.

Target Market(s)

Startups, (Small, medium and large corporates)

Industry/Entity Type

Business

Contact Information for Business Card

Name, Email, Address, Mobile number, Landline number, website

Colors

Designer to choose colors to be used in the design.

Requirements
Must have
• Nice new shape
Nice to have
• We want creative cuts, different size and impactful brand clarity
Should not have
• Boring and regular design and shape

```html
<!DOCTYPE html>
<html lang="en">
<head>
<meta charset="utf-8">
<title>Vandrel — Business Card</title>
<link rel="stylesheet" href="https://fonts.googleapis.com/css2?family=Open+Sans:wght@400;600&display=swap">
<style>
  :root {
    --brand-red: #ec1c24;
    --card-white: #ffffff;
    --frost: #ecebea;
    --frost-edge: #f7f6f5;
    --ghost-red: #f1b7b6;
    --ink: #1a1a1a;
    --backdrop: #e4e1de;
  }
  * { margin: 0; padding: 0; box-sizing: border-box; }
  html, body { width: 1200px; height: 900px; overflow: hidden; }
  body {
    background: var(--backdrop);
    position: relative;
    font-family: "Open Sans", Arial, sans-serif;
  }
  .card {
    position: absolute;
    display: flex;
    box-shadow: 0 6px 18px rgba(0,0,0,0.12);
  }
  .card--front { left: 78px; top: 34px; width: 588px; height: 364px; }
  .card--back { left: 388px; top: 505px; width: 567px; height: 352px; }

  .panel-red { background: var(--brand-red); position: relative; }
  .panel-white { background: var(--card-white); position: relative; }
  .card--front .panel-red { width: 355px; }
  .card--front .panel-white { flex: 1; }
  .card--back .panel-white { width: 227px; }
  .card--back .panel-red { flex: 1; }

  .window {
    position: absolute;
    background: var(--frost);
    border: 2px solid var(--frost-edge);
  }
  .card--front .window { left: 43px; top: 49px; width: 267px; height: 263px; }
  .card--back .window { left: 43px; top: 46px; width: 257px; height: 255px; }

  .brand-tile {
    position: absolute;
    background: var(--brand-red);
    display: flex;
    align-items: center;
    justify-content: center;
    gap: 10px;
    color: var(--card-white);
  }
  .card--front .brand-tile { left: 32px; top: 31px; width: 200px; height: 200px; }
  .brand-tile--ghost {
    left: 26px; top: 30px; width: 194px; height: 194px;
    background: var(--ghost-red);
    transform: scaleX(-1);
    opacity: 0.85;
  }
  .brand-mark {
    width: 16px; height: 16px;
    background: currentColor;
    flex: none;
  }
  .brand-name {
    font-weight: 600;
    font-size: 28px;
    letter-spacing: 1px;
    line-height: 1;
  }

  .holder { position: absolute; right: 38px; top: 34px; text-align: right; }
  .holder__name { color: var(--brand-red); font-weight: 600; font-size: 23px; line-height: 1.1; }
  .holder__role { color: var(--ink); font-size: 15px; line-height: 1.4; }
  .contact {
    position: absolute; right: 38px; top: 246px;
    list-style: none; text-align: right;
    color: var(--ink); font-size: 15px; line-height: 21px;
  }
</style>
</head>
<body>
  <article class="card card--front">
    <div class="panel-red">
      <div class="window">
        <div class="brand-tile">
          <span class="brand-mark"></span>
          <span class="brand-name">Vandrel</span>
        </div>
      </div>
    </div>
    <div class="panel-white">
      <div class="holder">
        <h1 class="holder__name">Arjun Mehra</h1>
        <p class="holder__role">Managing Director</p>
      </div>
      <ul class="contact">
        <li>022-480 315 672</li>
        <li>hello@vandrel.in</li>
        <li>www.vandrel.in</li>
      </ul>
    </div>
  </article>

  <article class="card card--back">
    <div class="panel-white"></div>
    <div class="panel-red">
      <div class="window">
        <div class="brand-tile brand-tile--ghost">
          <span class="brand-mark"></span>
          <span class="brand-name">Vandrel</span>
        </div>
      </div>
    </div>
  </article>
</body>
</html>
```